Awesome Design for a psychotherapy practise

We need a simple but modern design for a psychotherapy practise which opened recently. A logo, letterhead and a business card. Maybe something with the greek letter psi.

Font styles to use
Serif
Sans Serif

```html
<!DOCTYPE html>
<html lang="en">
<head>
<meta charset="utf-8">
<title>Letterhead – Psychotherapeutische Praxis</title>
<link rel="stylesheet" href="https://fonts.googleapis.com/css2?family=Open+Sans:wght@400;600&family=Montserrat:wght@400&display=swap">
<style>
  :root {
    --bg: #dcdcdc;
    --paper: #f8f8f8;
    --navy: #14284b;
    --body-text: #4a4a4a;
    --footer-text: #2b2b2b;
    --signature-tone: #e6e6e6;
  }
  * { margin: 0; padding: 0; box-sizing: border-box; }
  html, body {
    width: 1153px;
    height: 1200px;
    overflow: hidden;
    background: var(--bg);
  }
  .letterhead {
    position: absolute;
    left: 168px;
    top: 30px;
    width: 817px;
    height: 1140px;
    background: var(--paper);
    box-shadow: 0 6px 18px rgba(0,0,0,0.12);
    font-family: "Open Sans", sans-serif;
  }
  .wordmark {
    position: absolute;
    top: 76px;
    left: 0;
    right: 0;
    text-align: center;
    color: var(--navy);
    font-family: "Open Sans", sans-serif;
    font-weight: 600;
    text-transform: uppercase;
  }
  .wordmark-practice {
    font-size: 21px;
    letter-spacing: 1px;
    line-height: 26px;
  }
  .wordmark-name {
    font-size: 15px;
    letter-spacing: 5px;
    line-height: 20px;
  }
  .letter-body {
    position: absolute;
    left: 74px;
    width: 670px;
    color: var(--body-text);
    font-size: 15.2px;
    line-height: 22px;
  }
  .salutation { top: 270px; }
  .paragraph { text-align: justify; text-align-last: left; }
  .p1 { top: 314px; }
  .p2 { top: 446px; }
  .p3 { top: 578px; }
  .p4 { top: 710px; }
  .closing { top: 798px; }
  .signature {
    position: absolute;
    left: 76px;
    top: 848px;
    width: 94px;
    height: 89px;
    background: var(--signature-tone);
  }
  .contact {
    position: absolute;
    left: 0;
    right: 0;
    top: 1050px;
    text-align: center;
    font-family: "Montserrat", sans-serif;
    font-size: 14.6px;
    line-height: 22px;
    color: var(--footer-text);
  }
  .contact-line { display: flex; justify-content: center; align-items: center; gap: 10px; }
  .contact-item { display: inline-flex; align-items: center; gap: 5px; }
  .contact-item svg { width: 13px; height: 13px; fill: var(--navy); }
  .footer-band {
    position: absolute;
    left: 0;
    right: 0;
    bottom: 0;
    height: 17px;
    background: var(--navy);
  }
</style>
</head>
<body>
  <main class="letterhead">
    <header class="wordmark">
      <div class="wordmark-practice">Psychotherapeutische Praxis</div>
      <div class="wordmark-name">Dr. rer. nat. L. Wendrich</div>
    </header>

    <p class="letter-body salutation">Dear customer,</p>

    <p class="letter-body paragraph p1">Lorem ipsum dolor sit amet, consectetur adipisicing elit, sed do eiusmod tempor incididunt ut labore et dolore magna aliqua. Ut enim ad minim veniam, quis nostrud exercitation ullamco laboris nisi ut aliquip ex ea commodo consequat. Duis aute irure dolor in reprehenderit in voluptate velit esse cillum dolore eu fugiat nulla pariatur. Excepteur sint occaecat cupidatat non proident, sunt in culpa qui officia deserunt mollit anim id est laborum.</p>

    <p class="letter-body paragraph p2">Lorem ipsum dolor sit amet, consectetur adipisicing elit, sed do eiusmod tempor incididunt ut labore et dolore magna aliqua. Ut enim ad minim veniam, quis nostrud exercitation ullamco laboris nisi ut aliquip ex ea commodo consequat. Duis aute irure dolor in reprehenderit in voluptate velit esse cillum dolore eu fugiat nulla pariatur. Excepteur sint occaecat cupidatat non proident, sunt in culpa qui officia deserunt mollit anim id est laborum.</p>

    <p class="letter-body paragraph p3">Lorem ipsum dolor sit amet, consectetur adipisicing elit, sed do eiusmod tempor incididunt ut labore et dolore magna aliqua. Ut enim ad minim veniam, quis nostrud exercitation ullamco laboris nisi ut aliquip ex ea commodo consequat. Duis aute irure dolor in reprehenderit in voluptate velit esse cillum dolore eu fugiat nulla pariatur. Excepteur sint occaecat cupidatat non proident, sunt in culpa qui officia deserunt mollit anim id est laborum.</p>

    <p class="letter-body paragraph p4">Lorem ipsum dolor sit amet, consectetur adipisicing elit, sed do eiusmod tempor incididunt ut labore et dolore magna aliqua. Ut enim ad minim veniam, quis nostrud exercitation ullamco laboris nisi ut aliquip ex ea commodo consequat. Duis aute irure dolor in reprehenderit.</p>

    <p class="letter-body closing">Yours Sincerely,</p>

    <div class="signature" role="img" aria-label="Handwritten signature of the therapist"></div>

    <footer class="contact">
      <div class="contact-address">42 Lindenfeld Road Marlow, NJ 08123</div>
      <div class="contact-line">
        <span class="contact-item">
          <svg viewBox="0 0 24 24" aria-hidden="true"><path d="M6.6 10.8a15.1 15.1 0 0 0 6.6 6.6l2.2-2.2c.3-.3.7-.4 1-.2 1.1.4 2.3.6 3.6.6.6 0 1 .4 1 1V20c0 .6-.4 1-1 1A17 17 0 0 1 3 4c0-.6.4-1 1-1h3.5c.6 0 1 .4 1 1 0 1.3.2 2.5.6 3.6.1.3 0 .7-.2 1l-2.3 2.2z"/></svg>
          555 318 4072
        </span>
        <span class="contact-item">
          <svg viewBox="0 0 24 24" aria-hidden="true"><path d="M2 5h20v14H2z M4 7v.5l8 5 8-5V7l-8 5z" fill-rule="evenodd"/></svg>
          praxis.wendrich@mail.com
        </span>
        <span class="contact-item">
          <svg viewBox="0 0 24 24" aria-hidden="true"><path d="M12 2a10 10 0 1 0 0 20 10 10 0 0 0 0-20zm0 2a8 8 0 0 1 7.9 7h-3.5a13 13 0 0 0-2-6.6A8 8 0 0 1 12 4zm-2.4.4A13 13 0 0 0 7.6 11H4.1a8 8 0 0 1 5.5-6.6zM4.1 13h3.5a13 13 0 0 0 2 6.6A8 8 0 0 1 4.1 13zm5.5 0h4.8a11 11 0 0 1-2.4 6.3A11 11 0 0 1 9.6 13zm0-2a11 11 0 0 1 2.4-6.3 11 11 0 0 1 2.4 6.3zm4.8 8.6a13 13 0 0 0 2-6.6h3.5a8 8 0 0 1-5.5 6.6z"/></svg>
          www.praxis-wendrich.com
        </span>
      </div>
    </footer>

    <div class="footer-band"></div>
  </main>
</body>
</html>
```